Fahrzeugbeschriftung für Hersteller von Campingzubehör
Zielgruppe
Wir sind Hersteller von Campingzubehör, made in Germany! Angesprochen werden sollen, Camper, Händler und Vermieter von Freizeitfahrzeugen. Hier soll ein Sonnensegel kreiert werden, als Werbemaßnahme für die o.g. Zielgruppe. Dieses Sonnensegel soll auf die Einzigartigkeit des Campers wieder spiegeln. Für den schönsten Schatten der Welt!
Campen ist IN! und Individualität wird groß geschrieben. Das Alter der Zielgruppe reicht von 42-80 und legt Wert auf Nachhaltigkeit, Qualität, schätzt den Komfort, aber eben auch das Hobby und die damit verbundene Reiselust.
Aufgabenstellung
Druckformat ist eines 3m breit und 2,2m hoch und 1m breit und 2,2m hoch, Druckvorlage ist dabei. Wichtig ist die HP
www.zeltmarktwaren.com
Das Banner soll dann aussehen wie dies auf der erste Seite des Flyers

```html
<!DOCTYPE html>
<html lang="de">
<head>
<meta charset="utf-8">
<title>Sunblocker Banner – Zeltmarkt Waren</title>
<link rel="stylesheet" href="https://fonts.googleapis.com/css2?family=Open+Sans:wght@400;600&display=swap">
<style>
  :root {
    --page: #ffffff;
    --sky: #9fe6dc;
    --tree: #6f9a4a;
    --grass: #5fb82f;
    --grass-deep: #4ea626;
    --leaf: #9ec64f;
    --signal-yellow: #f3f01a;
    --ink: #111111;
    --white: #ffffff;
    --camper: #e9ecec;
    --print-warm: #a66a3a;
    --print-green: #7fb45a;
  }
  html, body {
    margin: 0;
    padding: 0;
    width: 1200px;
    height: 2640px;
    overflow: hidden;
    background: var(--page);
  }
  .canvas {
    position: relative;
    width: 1200px;
    height: 2640px;
    font-family: "Open Sans", Arial, sans-serif;
    color: var(--ink);
  }
  .artwork {
    position: absolute;
    inset: 0;
    width: 1200px;
    height: 2640px;
  }
  .badge-new {
    position: absolute;
    left: 428px;
    top: 1462px;
    margin: 0;
    font-size: 158px;
    font-weight: 600;
    line-height: 1;
    color: var(--signal-yellow);
    letter-spacing: -2px;
  }
  .headline {
    position: absolute;
    left: 282px;
    top: 1676px;
    margin: 0;
    font-size: 66px;
    font-weight: 400;
    line-height: 84px;
    letter-spacing: 0.5px;
  }
  .tagline {
    position: absolute;
    left: 288px;
    top: 2006px;
    margin: 0;
    font-size: 48px;
    font-weight: 400;
    line-height: 64px;
  }
  .brand-name {
    position: absolute;
    left: 822px;
    top: 1842px;
    margin: 0;
    font-size: 34px;
    font-weight: 600;
    line-height: 1;
    color: var(--leaf);
  }
</style>
</head>
<body>
<div class="canvas">
  <svg class="artwork" viewBox="0 0 1175 2588" preserveAspectRatio="none" xmlns="http://www.w3.org/2000/svg">
    <defs>
      <linearGradient id="sceneGradient" x1="0" y1="0" x2="0" y2="1">
        <stop offset="0" stop-color="var(--sky)"/>
        <stop offset="0.14" stop-color="#b8e3d6"/>
        <stop offset="0.2" stop-color="var(--tree)"/>
        <stop offset="0.27" stop-color="var(--grass)"/>
        <stop offset="1" stop-color="var(--grass-deep)"/>
      </linearGradient>
      <linearGradient id="printGradient" x1="0" y1="0" x2="1" y2="0">
        <stop offset="0" stop-color="var(--print-green)"/>
        <stop offset="0.5" stop-color="var(--print-warm)"/>
        <stop offset="1" stop-color="#c9d9b0"/>
      </linearGradient>
      <filter id="panelShadow" x="-5%" y="-5%" width="110%" height="110%">
        <feDropShadow dx="0" dy="4" stdDeviation="10" flood-color="#000" flood-opacity="0.35"/>
      </filter>
    </defs>

    <g class="banner-panel" filter="url(#panelShadow)">
      <rect x="58" y="120" width="1060" height="2332" fill="var(--grass-deep)"/>
    </g>

    <rect class="scene-photo" x="58" y="120" width="1060" height="2332" fill="url(#sceneGradient)"
          role="img" aria-label="Foto: Wiese mit Bäumen und blauem Himmel im Hintergrund"/>

    <rect class="camper-photo" x="134" y="450" width="942" height="350" rx="18" fill="var(--camper)"
          role="img" aria-label="Foto: weißes Reisemobil mit ausgefahrener Markise"/>

    <rect class="sunblocker-print" x="180" y="512" width="572" height="388" fill="url(#printGradient)"
          role="img" aria-label="Foto: bedruckter Sunblocker mit Hundemotiv in einer Blumenwiese"/>

    <path class="accent-band" d="M1118 1000 C 600 1020, 80 1600, 58 2452 L1118 2452 Z" fill="var(--signal-yellow)"/>
    <path class="leaf-field" d="M1118 1065 C 640 1090, 110 1640, 92 2452 L1118 2452 Z" fill="var(--leaf)"/>
    <path class="brand-field" d="M1118 1228 C 850 1420, 742 1700, 755 1880 C 770 2100, 900 2300, 1118 2452 Z" fill="var(--white)"/>
  </svg>

  <p class="badge-new">NEU</p>
  <h1 class="headline">INDIVIDUELL<br>BEDRUCKBARE<br>SUNBLOCKER</h1>
  <p class="tagline">Für den schönsten<br>Schatten der Welt</p>
  <p class="brand-name">Zeltmarkt Waren</p>
</div>
</body>
</html>
```